Flyer Rework for Accountants and Lawyers

Information flyer for accountants and lawyers. Text and flowchart provided. Just need to make it look presentable for print and email. Needs to add logo (AI file provided) and provide graphics. No more than two pages. Our corporate visual identify guidelines are attached (MUST Use). Completed on both AI file and PPTX file.
Target Market(s)
Accountants, Company Directors and Lawyers
Industry/Entity Type
Finance And Accounting
Requirements
Must have
- Our corporate visual identify guidelines are attached (MUST Use)

```html
<!DOCTYPE html>
<html lang="en">
<head>
<meta charset="utf-8">
<title>Director Penalty Notices – Fernbrook Advisory</title>
<link rel="stylesheet" href="https://fonts.googleapis.com/css2?family=Source+Sans+3:wght@300;400;600;700&display=swap">
<style>
:root{
  --green:#5bb947;
  --blue:#5fc6e0;
  --grey:#6b6b6d;
  --text:#8a8a8c;
  --dark:#3c3c3e;
  --row:#f2f2f2;
  --band:#efefef;
  --backdrop:#b9b9b9;
}
*{margin:0;padding:0;box-sizing:border-box}
html,body{width:1200px;height:1200px;overflow:hidden}
body{background:radial-gradient(circle at 50% 45%,#d0d0d0,var(--backdrop));font-family:"Source Sans 3",sans-serif;color:var(--text);position:relative}
.page{position:absolute;left:257px;width:840px;height:594px;background:#fff;overflow:hidden;transform:scale(.8);transform-origin:0 0;box-shadow:0 3px 12px rgba(0,0,0,.18)}
.page-front{top:94px}
.page-back{top:633px}
.abs{position:absolute}
.brand{display:flex;align-items:center;gap:8px}
.brand-mark{width:64px;height:64px;border-radius:50%;border:6px solid var(--grey);flex:none}
.brand-name{color:var(--green);font-weight:600;font-size:17px;letter-spacing:.3px;text-transform:uppercase;white-space:nowrap}
.values{left:18px;top:112px;display:flex;align-items:center;gap:5px;font-weight:700;font-size:24px;color:var(--green);white-space:nowrap}
.values .icon{width:24px;height:24px;border-radius:50%;border:3px solid var(--green);margin-left:3px;flex:none}
.intro{left:18px;top:150px;width:490px;font-size:11px;line-height:15px}
.tab{position:absolute;color:#fff;font-weight:600;font-size:14.5px;padding:4px 16px 4px 17px;line-height:20px;white-space:nowrap}
.tab-blue{background:var(--blue)}
.tab-green{background:var(--green)}
.body-copy{font-size:11px;line-height:15px}
.lead{left:15px;top:305px;font-size:12.5px;color:var(--dark)}
.lead b{color:var(--green)}
.facts{left:15px;top:339px;width:810px;border-collapse:collapse;font-size:8.3px;color:var(--grey)}
.facts th{color:#fff;font-weight:600;font-size:14px;text-align:left;padding:3px 9px;height:24px}
.facts th.col-fact{background:var(--blue);width:122px}
.facts th.col-key{background:#6b6b6d}
.facts td{padding:4px 9px;vertical-align:middle;line-height:10.5px}
.facts tr:nth-child(odd) td{background:var(--row)}
.facts .dot{display:inline-block;width:6px;height:6px;border-radius:50%;background:var(--green);margin:0 6px 0 2px}
.band{position:absolute;background:var(--band)}
.tips{left:16px;top:62px;width:570px;list-style:none}
.tips li{position:relative;padding-left:14px;margin-bottom:14px;font-size:11px;line-height:14px}
.tips li::before{content:"";position:absolute;left:2px;top:4px;width:6px;height:6px;border-radius:50%;background:var(--green)}
.tips b{color:var(--green);font-weight:600}
.step{position:absolute;display:flex;align-items:center;justify-content:center;text-align:center;color:#fff;font-size:11.5px;line-height:15px;border:5px solid #fff;outline:1px solid #ddd;padding:6px 10px}
.step > div{width:100%}
.step-blue{background:var(--blue)}
.step-green{background:var(--green)}
.step ol{text-align:left;padding-left:16px;margin-top:4px}
.arrow{position:absolute}
.label{position:absolute;color:var(--green);font-weight:600;font-size:11px}
.help{left:17px;top:525px;width:810px;font-size:11px;line-height:15px}
.help b{color:var(--green)}
</style>
</head>
<body>

<section class="page page-front">
  <svg class="abs" style="left:515px;top:-10px" width="340" height="290" role="img" aria-label="Photo of a smiling team applauding in an office">
    <defs>
      <linearGradient id="teamTone" x1="0" y1="0" x2="1" y2="1">
        <stop offset="0" stop-color="#3a4a4f"/><stop offset=".55" stop-color="#8a6d55"/><stop offset="1" stop-color="#e6e2a8"/>
      </linearGradient>
    </defs>
    <circle cx="180" cy="120" r="158" fill="none" stroke="var(--grey)" stroke-width="10"/>
    <path d="M24 140 A158 158 0 0 0 338 140" fill="none" stroke="var(--green)" stroke-width="10"/>
    <circle cx="180" cy="120" r="150" fill="url(#teamTone)"/>
  </svg>

  <div class="abs brand" style="left:17px;top:18px">
    <span class="brand-mark"></span>
    <span class="brand-name">Fernbrook Advisory</span>
  </div>

  <div class="abs values">
    <span class="icon"></span>INDEPENDENT<span class="icon"></span>CONCISE<span class="icon"></span>EFFICIENT
  </div>

  <p class="abs intro">Company directors and their advisors need to be aware that non-lodgement of Business Activities Statements (“BAS”) and Superannuation Guarantee Charge (“SCG”) Statements with the ATO may be personally liability for these debts.</p>

  <div class="tab tab-blue" style="left:15px;top:207px;padding:4px 9px">Director Penalty Notices (“DPN”)</div>

  <p class="abs body-copy" style="left:16px;top:246px;width:515px">The ATO uses DPNs and Garnishee Notices to recovery tax debts and to impose positive obligations on Directors to deal with outstanding PAYG Withholding and the Superannuation Guarantee Charge debts (“Tax Debts”).</p>

  <p class="abs lead">The DPN regime makes directors of companies who fail to pay Tax Debts <b>personally liable.</b> The key facts of DPN regime are outlined below:</p>

  <table class="abs facts">
    <tr><th class="col-fact">Facts</th><th class="col-key">Key facts of a Directors Penalty Notice</th></tr>
    <tr style="height:42px"><td>Director personal liabilities</td><td>Directors become personally liable for Tax Debts 21 days are the DPN Notice is issued</td></tr>
    <tr style="height:48px"><td>Automatic liability for unreported and unpaid Tax Debts</td><td>Where a company’s Tax Debts were both unreported and unpaid 3 months after the due date, the directors are automatically personally liable for the Tax Debts.</td></tr>
    <tr style="height:54px"><td>Avoiding personal liability for directors once they receive a DPN</td><td>Within 21 days of issuing the DPN (which may be received a week or more after issue), a director can avoid personal liability by either:<br><br><span class="dot"></span>Paying the Tax Debt &nbsp; <span class="dot"></span>Appointing an Administrator to the company &nbsp; <span class="dot"></span>Appointing a Liquidator to the company.</td></tr>
    <tr style="height:42px"><td>Effect on new directors</td><td>New directors are liable if outstanding Tax Debts are unpaid 30 days after their appointment as director</td></tr>
    <tr style="height:26px"><td>Time frames</td><td>ATO can only enforce a DPN after 21 days of giving notice to the director and notice can be given to the company tax agent</td></tr>
  </table>
</section>

<section class="page page-back">
  <div class="band" style="left:0;top:38px;width:840px;height:148px"></div>
  <svg class="abs" style="left:595px;top:-20px" width="260" height="240" role="img" aria-label="Photo of a businessman signing documents beside scales of justice">
    <defs>
      <linearGradient id="deskTone" x1="0" y1="0" x2="1" y2="1">
        <stop offset="0" stop-color="#b07a3a"/><stop offset=".5" stop-color="#2e2a28"/><stop offset="1" stop-color="#6a5a4a"/>
      </linearGradient>
    </defs>
    <circle cx="130" cy="105" r="118" fill="none" stroke="var(--grey)" stroke-width="9"/>
    <path d="M12 115 A118 118 0 0 0 248 115" fill="none" stroke="var(--green)" stroke-width="9"/>
    <circle cx="130" cy="105" r="111" fill="url(#deskTone)"/>
  </svg>

  <div class="tab tab-blue" style="left:0;top:20px">Tips for directors to limit or avoid personal liability:</div>

  <ul class="abs tips">
    <li><b>Always lodge BAS and SGC Statements within 3 months of the due date,</b> even if the liability cannot be paid!</li>
    <li>Act immediately upon receipt of a <b>DPN and consider a payment arrangement with the ATO.</b> This should be considered with care as payments made can be considered as preference payments to the ATO, if a liquidator is appointed. The ATO can make the directors personally liable for the ATO preference claim</li>
    <li><b>Seek professional advice from an insolvency practitioner</b> about the options available and possibly save the company through a financial restructure.</li>
  </ul>

  <div class="tab tab-green" style="left:0;top:201px">Summary of the DPN</div>

  <div class="step step-blue" style="left:16px;top:261px;width:148px;height:89px"><div>Issued Director’s Penalty Notice By ATO</div></div>
  <div class="step step-blue" style="left:197px;top:240px;width:148px;height:225px;font-weight:600"><div>Business Activity Statement and Superannuation Guarantee Charge lodged within 3 months from due date</div></div>
  <div class="step step-green" style="left:384px;top:240px;width:148px;height:101px"><div>Director not personally liable yet.<br>(Have options) <b>RIGHTS</b></div></div>
  <div class="step step-green" style="left:384px;top:365px;width:148px;height:97px"><div>Director Automatically <b>personally liable</b></div></div>
  <div class="step step-blue" style="left:575px;top:240px;width:248px;height:101px">
    <div style="text-align:left"><b style="display:block;text-align:center">If Directors act within 21 days and:</b>
      <ol><li>Wind up Company voluntarily; or</li><li>Appoint Voluntary Administrator; or</li><li>Pay debt in full</li></ol></div>
  </div>
  <div class="step step-blue" style="left:633px;top:374px;width:148px;height:91px"><div>Director <b>not</b> personally liable but the company is still insolvent.</div></div>

  <svg class="arrow" style="left:0;top:0" width="840" height="594" aria-hidden="true">
    <g fill="var(--green)">
      <path d="M170 295h14v-6l10 9-10 9v-6h-14z"/>
      <path d="M359 291l14-4-2-6 12 3-7 11-1-5-14 4z"/>
      <path d="M359 372l12 8 3-5 3 12-12-1 4-4-12-8z"/>
      <path d="M544 281h14v-6l10 9-10 9v-6h-14z"/>
      <path d="M598 340h6v12h5l-8 10-8-10h5z"/>
      <path d="M703 345h6v12h5l-8 10-8-10h5z"/>
      <path d="M598 378h6v12h5l-8 10-8-10h5z"/>
      <path d="M600 416h-12v-5l-9 8 9 8v-5h12z"/>
      <path d="M565 418h-12v-5l-9 8 9 8v-5h12z"/>
    </g>
  </svg>
  <div class="label" style="left:722px;top:352px">Yes</div>
  <div class="label" style="left:561px;top:382px">No</div>

  <div class="abs brand" style="left:18px;top:395px;gap:6px">
    <span class="brand-mark" style="width:42px;height:42px;border-width:4px"></span>
    <span class="brand-name" style="font-size:10px;letter-spacing:0">Fernbrook Advisory</span>
  </div>

  <div class="band" style="left:0;top:500px;width:840px;height:94px"></div>
  <div class="tab tab-green" style="left:0;top:485px">How Fernbrook Advisory can help?</div>
  <p class="abs help">Fernbrook Advisory is a firm that specialises in insolvency and restructuring, we are here to assist your clients who experiencing financial difficulties with straight forward solutions in simple to understand terms. The initial consultation is free, strictly confidential and without obligation. Please call (02) 5550 1234 to speak to one of our solvency specialistor email <b>info@fernbrookadvisory.example</b></p>
</section>

</body>
</html>
```